Kelmora Legal Business Card

I require a corporate business card for a new legal services business.

I do not have a logo, nor do I want one.

I require a clean, neat a professional card for a law firm.

Details:

Business Name: Kelmora Legal
Name: Debra Lindqvist
Title: Corporate Services Manager
Location: Office 14 (Top Floor), Toravel Business Centre, Quinlan Grove Street, Alotau CBD, Milne Bay Province.
Postal Address: PO Box 593, Alotau, 211, Milne Bay Province, Papua New Guinea.
Contact: T: +675 6418250, F: +675 6413362, M: +675 72915867, E: dlindqvist@kelmoraexample.com.pg.

I look forward to your design submissions.

Industry/Entity Type

Legal

```html
<!DOCTYPE html>
<html lang="en">
<head>
<meta charset="utf-8">
<title>Kelmora Legal Business Card</title>
<link rel="stylesheet" href="https://fonts.googleapis.com/css2?family=Open+Sans:wght@400;600;700&display=swap">
<style>
  :root {
    --backdrop: #b9b9b9;
    --panel-dark: #2b2b2b;
    --panel-light: #f7f7f5;
    --accent-green: #6cb33f;
    --accent-green-dark: #4f8f26;
    --text-light: #ffffff;
    --text-muted: #c9c9c9;
    --text-dark: #1e1e1e;
    --divider: #454545;
  }
  html, body {
    margin: 0;
    width: 1200px;
    height: 900px;
    overflow: hidden;
    background: var(--backdrop);
    font-family: "Open Sans", Arial, sans-serif;
  }
  .business-card {
    position: absolute;
    left: 150px;
    top: 193px;
    width: 900px;
    height: 514px;
    display: flex;
    box-shadow: 0 8px 24px rgba(0,0,0,0.25);
  }
  .contact-panel {
    position: relative;
    width: 410px;
    height: 100%;
    background: var(--panel-dark);
    color: var(--text-muted);
  }
  .person-name {
    position: absolute;
    left: 60px;
    top: 52px;
    margin: 0;
    font-size: 30px;
    font-weight: 700;
    color: var(--text-light);
  }
  .person-title {
    position: absolute;
    left: 40px;
    top: 94px;
    margin: 0;
    font-size: 23px;
    line-height: 27px;
    font-weight: 400;
    color: var(--accent-green);
  }
  .contact-row {
    position: absolute;
    left: 0;
    width: 410px;
    border-bottom: 1px solid var(--divider);
  }
  .row-address { top: 168px; height: 120px; }
  .row-phone { top: 289px; height: 92px; }
  .row-email { top: 382px; height: 72px; border-bottom: none; }
  .row-text {
    position: absolute;
    left: 40px;
    margin: 0;
    font-style: normal;
  }
  .address-text {
    top: 10px;
    width: 290px;
    font-size: 12px;
    line-height: 21px;
  }
  .phone-text {
    top: 10px;
    font-size: 22px;
    line-height: 25px;
    color: var(--text-muted);
  }
  .email-text {
    top: 20px;
    font-size: 18px;
    color: var(--text-muted);
  }
  .icon-tab {
    position: absolute;
    right: 0;
    width: 64px;
    height: 60px;
    background: var(--accent-green);
    border-bottom: 3px solid var(--accent-green-dark);
    display: flex;
    align-items: center;
    justify-content: center;
  }
  .row-address .icon-tab { top: 58px; }
  .row-phone .icon-tab { top: 16px; }
  .row-email .icon-tab { top: 6px; }
  .brand-panel {
    flex: 1;
    background: var(--panel-light);
    display: flex;
    flex-direction: column;
    align-items: center;
    justify-content: center;
  }
  .brand-name {
    margin: 0;
    font-size: 50px;
    line-height: 58px;
    font-weight: 700;
    color: var(--text-dark);
    text-align: center;
  }
  .brand-rule {
    width: 250px;
    height: 1px;
    background: var(--text-dark);
    margin: 40px 0 10px;
  }
  .brand-tagline {
    margin: 0;
    width: 250px;
    font-size: 17px;
    line-height: 21px;
    font-weight: 700;
    color: var(--text-dark);
    text-align: center;
  }
</style>
</head>
<body>
  <div class="business-card">
    <section class="contact-panel">
      <h1 class="person-name">Debra Lindqvist</h1>
      <p class="person-title">Corporate Services<br>Manager</p>

      <div class="contact-row row-address">
        <address class="row-text address-text">Office 14 (Top Floor), Toravel Business Centre, Quinlan Grove Street, Alotau CBD, Milne Bay Province. PO Box 593, Alotau, 211, Milne Bay Province, Papua New Guinea.</address>
        <div class="icon-tab">
          <svg width="30" height="28" viewBox="0 0 30 28" aria-hidden="true">
            <path d="M3 14 L15 3 L27 14" fill="none" stroke="#fff" stroke-width="3" stroke-linejoin="round"/>
            <path d="M7 12 V25 H13 V18 H17 V25 H23 V12" fill="#fff"/>
          </svg>
        </div>
      </div>

      <div class="contact-row row-phone">
        <p class="row-text phone-text">675.641.8250<br>675.641.3362<br>675.729.15867</p>
        <div class="icon-tab">
          <svg width="28" height="28" viewBox="0 0 28 28" aria-hidden="true">
            <path d="M3 10 Q14 2 25 10 L22 13 L18 11 V8 Q14 6 10 8 V11 L6 13 Z" fill="#fff"/>
            <rect x="6" y="14" width="16" height="10" rx="2" fill="none" stroke="#fff" stroke-width="2.5"/>
            <circle cx="14" cy="19" r="2.5" fill="#fff"/>
          </svg>
        </div>
      </div>

      <div class="contact-row row-email">
        <p class="row-text email-text">dlindqvist@kelmoraexample.com.pg</p>
        <div class="icon-tab">
          <svg width="30" height="26" viewBox="0 0 30 26" aria-hidden="true">
            <rect x="3" y="3" width="24" height="15" fill="none" stroke="#fff" stroke-width="3"/>
            <rect x="12" y="18" width="6" height="4" fill="#fff"/>
            <rect x="8" y="22" width="14" height="2.5" fill="#fff"/>
          </svg>
        </div>
      </div>
    </section>

    <section class="brand-panel">
      <h2 class="brand-name">Kelmora<br>Legal</h2>
      <div class="brand-rule"></div>
      <p class="brand-tagline">Your Text HereYour Text Here</p>
    </section>
  </div>
</body>
</html>
```